Sign Advertisment for Condominium Development

I need a sign created that will be placed in front of a building that is being converted into a luxury condominium development.

The sign needs to say:

Two, Boutique Luxury Condominiums Delivering late 2015.

Luxury Finishes // Designer Kitchens and Bath // Each Unit over 2,000 Square Feet

Deeded Parking Included with Each Unit

To Learn More, Contact:

Loretta Pinwell or Morgan Tesh
(202) 555-0147
Loretta.Pinwell@nrg-example.com

I need a small disclaimer at the bottom stating:

These Condominium(s) have not been registered by the Office of Residential Property Oversight Bureau of Dwelling Registration Tenancy Transfer and Purchase Section. A Condominium Unit may be reserved on a non-binding reservation agreement, but no contract of sale or lease that is binding on the purchaser may be entered into prior to registration.

Target Market(s)

Young professionals seeking luxury condominium

Industry/Entity Type

Building

Font styles to use
Serif

Colors
00a88f
ffffff

```html
<!DOCTYPE html>
<html lang="en">
<head>
<meta charset="utf-8">
<title>Boutique Luxury Condominiums – Sign</title>
<link rel="stylesheet" href="https://fonts.googleapis.com/css2?family=Abril+Fatface&family=Bodoni+Moda:opsz,wght@6..96,800&family=Tinos:wght@400;700&display=swap">
<style>
  :root {
    --paper: #ffffff;
    --ink: #111111;
    --accent-red: #e3202b;
    --band-teal: #00a88f;
    --band-text: #ffffff;
  }
  html, body {
    margin: 0;
    padding: 0;
    overflow: hidden;
    background: var(--paper);
  }
  .sign {
    position: relative;
    width: 1192px;
    height: 1200px;
    background: var(--paper);
    overflow: hidden;
    color: var(--ink);
    font-family: "Tinos", "Times New Roman", serif;
  }
  .disclaimer-band {
    position: absolute;
    left: 0;
    top: 999px;
    width: 1192px;
    height: 201px;
    background: var(--band-teal);
  }
  .frame {
    position: absolute;
    left: 21px;
    top: 36px;
    width: 1151px;
    height: 1138px;
    box-sizing: border-box;
    border: 6px solid var(--accent-red);
    border-radius: 26px;
    z-index: 3;
    pointer-events: none;
  }
  .unit-count {
    position: absolute;
    left: 62px;
    top: 6px;
    margin: 0;
    font-family: "Abril Fatface", "Bodoni Moda", serif;
    font-size: 390px;
    line-height: 1;
    font-weight: 400;
  }
  .headline {
    position: absolute;
    left: 286px;
    top: 112px;
    margin: 0;
    font-family: "Bodoni Moda", "Abril Fatface", serif;
    font-weight: 800;
    font-size: 96px;
    line-height: 92px;
    letter-spacing: 0.5px;
  }
  .delivery {
    position: absolute;
    left: 278px;
    top: 348px;
    margin: 0;
    font-weight: 700;
    font-size: 44px;
  }
  .features {
    position: absolute;
    left: 0;
    top: 440px;
    width: 1192px;
    margin: 0;
    padding: 0;
    list-style: none;
    text-align: center;
    color: var(--accent-red);
    font-weight: 700;
    font-size: 45px;
    line-height: 63px;
  }
  .contact-label {
    position: absolute;
    left: 64px;
    top: 790px;
    margin: 0;
    font-weight: 700;
    font-size: 26px;
  }
  .contact-details {
    position: absolute;
    left: 416px;
    top: 790px;
    margin: 0;
    font-style: normal;
    font-weight: 700;
    font-size: 48px;
    line-height: 64px;
  }
  .contact-details .email { font-size: 42px; }
  .disclaimer {
    position: absolute;
    left: 0;
    top: 1014px;
    width: 1192px;
    margin: 0;
    text-align: center;
    color: var(--band-text);
    font-size: 22px;
    line-height: 31px;
    z-index: 2;
  }
</style>
</head>
<body>
  <main class="sign">
    <div class="disclaimer-band"></div>
    <div class="frame"></div>

    <p class="unit-count" aria-label="Two">2</p>
    <h1 class="headline">Boutique Luxury<br>Condominiums</h1>
    <p class="delivery">Delivering late 2015</p>

    <ul class="features">
      <li>Luxury Finishes</li>
      <li>Designer Kitchens and Bath</li>
      <li>Each Unit over 2,000 Square Feet</li>
      <li>Deeded Parking Included with Each Unit</li>
    </ul>

    <p class="contact-label">To Learn More, Contact:</p>
    <address class="contact-details">
      <div class="names">Loretta Pinwell or Morgan Tesh</div>
      <div class="phone">(202) 555-0147</div>
      <div class="email">Loretta.Pinwell@nrg-example.com</div>
    </address>

    <p class="disclaimer">
      These Condominium(s) have not been registered by the Office of Residential Property Oversight<br>
      Bureau of Dwelling Registration Tenancy Transfer and Purchase Section.<br>
      A Condominium Unit may be reserved on a non-binding reservation agreement,<br>
      but no contract of sale or lease that is binding on the purchaser may be entered into prior to registration.
    </p>
  </main>
</body>
</html>
```